Business Cards for a company that provides webstore services to veterinarians

We need business cards designed for our main service PawCartHub. PawCartHub is a webstore that veterinarian clinics can use to that will allow their clients to purchase products for their pets. Our company is Brindlow Veterinary Solutions (BVS). Our mission statement is We love pets! We will do everything possible to facilitate along, healthy and happy relationship with their families.

Target Market(s)

Veterinarians

Industry/Entity Type

Veterinary

Contact Information for Business Card

I would like the design to incorporate the colours our our company. Cards should have room for employee name, title (only necessary in two instances), phone number, mobile number, email address and linkedin symbol and related profile name ie Marla Quinton. I would like the PawCartHub logo to appear on one side and BVS logo to appear on the other. I will need both an english and french version. I can provide the french translation. Please focus on english version and then we will translate

Colors

Designer to choose colors to be used in the design.

Requirements
Must have
• one side - PawCartHub logo with persons name, phone number, mobile number, email address
• second side - BVS logo
• colours should be consistent with our company. colours are as follows:
• Red
• RGB: 190 / 30 / 45
• CYMK: 14 / 100 / 90 /10
• Hex: #BE1E2D
• Gray
• RGB: 88 / 89 / 86
• CYMK: 3 / 2 / 0 /64
• Hex: #585956
Nice to have
• address of company - can be on either side address is 4817 Feldmoor Street Suite 305 Burlington ON K2R 6T4. Toll free number will vary depending on person
• Linkedin symbol and name of person
• on second side with BVS logo our company's mission statement
Should not have
• nothing comes to mind

```html
<!DOCTYPE html>
<html lang="en">
<head>
<meta charset="utf-8">
<title>PawCartHub Business Card</title>
<link href="https://fonts.googleapis.com/css2?family=Lato:ital,wght@0,400;0,700;0,900;1,400;1,700&display=swap" rel="stylesheet">
<style>
  :root {
    --brand-red: #BE1E2D;
    --brand-gray: #585956;
    --ink: #1d1d1d;
    --paper: #ffffff;
    --canvas: #eeeeee;
  }
  * { box-sizing: border-box; margin: 0; padding: 0; }
  html, body {
    width: 1200px; height: 586px; overflow: hidden;
    background: var(--canvas);
    font-family: "Lato", sans-serif;
  }
  .stage { position: relative; width: 1200px; height: 586px; }
  .card {
    position: absolute; top: 142px;
    width: 502px; height: 301px; overflow: hidden;
  }
  /* Front side */
  .card--front { left: 61px; background: var(--brand-red); color: var(--paper); }
  .front-brand {
    position: absolute; left: 0; right: 0; top: 112px;
    text-align: center; font-size: 46px; font-weight: 400;
    letter-spacing: -0.5px; color: var(--paper);
  }
  .front-social {
    position: absolute; left: 0; right: 0; top: 258px;
    display: flex; justify-content: center; align-items: center; gap: 5px;
    font-size: 12.5px; font-weight: 700;
  }
  .front-social__mark { width: 13px; height: 13px; background: var(--paper); border-radius: 2px; }

  /* Back side */
  .card--back { left: 619px; background: var(--paper); color: var(--ink); }
  .person { position: absolute; left: 29px; top: 34px; }
  .person__name { font-size: 17px; font-weight: 700; color: var(--brand-red); }
  .person__title { font-size: 11px; font-style: italic; margin-top: 3px; }
  .address {
    position: absolute; left: 29px; top: 106px;
    font-size: 12px; font-weight: 700; font-style: normal;
    color: var(--brand-red); line-height: 18px;
  }
  .contacts { position: absolute; left: 29px; top: 180px; list-style: none; }
  .contacts li {
    display: flex; align-items: center; gap: 8px;
    font-size: 12px; height: 22.5px;
  }
  .contacts svg { width: 18px; height: 18px; flex: none; }
  .company-name {
    position: absolute; left: 290px; width: 170px; top: 70px;
    display: flex; align-items: center; gap: 9px;
    font-size: 17px; font-weight: 700; line-height: 21px;
    color: var(--brand-red);
  }
  .company-name__dot { width: 12px; height: 12px; border-radius: 50%; background: var(--brand-red); flex: none; }
  .swoosh { position: absolute; left: 0; top: 0; width: 502px; height: 301px; }
  .footer-web {
    position: absolute; left: 29px; top: 280px;
    font-size: 12px; font-weight: 700; letter-spacing: 1.2px; color: var(--paper);
  }
  .footer-motto {
    position: absolute; right: 30px; top: 275px;
    font-size: 15px; font-weight: 700; font-style: italic; letter-spacing: 0.8px; color: var(--paper);
  }
</style>
</head>
<body>
<main class="stage">
  <section class="card card--front" aria-label="Card front">
    <div class="front-brand">PawCartHub</div>
    <div class="front-social">
      <span class="front-social__mark"></span>
      <span>/pawcarthub.ca</span>
    </div>
  </section>

  <section class="card card--back" aria-label="Card back">
    <svg class="swoosh" viewBox="0 0 502 301" aria-hidden="true">
      <path d="M110 268 C 250 262, 400 240, 502 216 L 502 242 C 400 258, 250 266, 110 268 Z" fill="var(--brand-gray)"/>
      <path d="M0 275 L 120 275 C 280 272, 420 258, 502 241 L 502 301 L 0 301 Z" fill="var(--brand-red)"/>
    </svg>

    <div class="person">
      <div class="person__name">Marla Quinton</div>
      <div class="person__title">Owner &amp; Founder</div>
    </div>

    <address class="address">
      4817 Feldmoor Street Suite,<br>
      305 Burlington ON K2R 6T4
    </address>

    <ul class="contacts">
      <li>
        <svg viewBox="0 0 18 18" aria-hidden="true"><circle cx="9" cy="9" r="9" fill="var(--brand-red)"/><path d="M4.5 8 Q9 4 13.5 8 L12.5 9.3 L10.8 8.4 L10.8 7.4 Q9 6.8 7.2 7.4 L7.2 8.4 L5.5 9.3 Z M6 10 H12 L12.6 13 H5.4 Z" fill="#fff"/></svg>
        <span>+1 905 555 0142</span>
      </li>
      <li>
        <svg viewBox="0 0 18 18" aria-hidden="true"><circle cx="9" cy="9" r="9" fill="var(--brand-red)"/><rect x="6" y="3.5" width="6" height="11" rx="1" fill="#fff"/><rect x="7" y="5" width="4" height="7" fill="var(--brand-red)"/></svg>
        <span>+1 905 555 - 0187</span>
      </li>
      <li>
        <svg viewBox="0 0 18 18" aria-hidden="true"><circle cx="9" cy="9" r="9" fill="var(--brand-red)"/><rect x="4.5" y="5.5" width="9" height="7" fill="#fff"/><path d="M4.5 5.5 L9 9.5 L13.5 5.5" fill="none" stroke="var(--brand-red)" stroke-width="1"/></svg>
        <span>mquinton@brindlowvs.ca</span>
      </li>
    </ul>

    <div class="company-name">
      <span class="company-name__dot"></span>
      <span>Brindlow Veterinary Solutions</span>
    </div>

    <div class="footer-web">www.pawcarthub.ca</div>
    <div class="footer-motto">We Love Pets</div>
  </section>
</main>
</body>
</html>
```